Flyer for an IT consultancy firm

We are an IT consultancy firm based in Iceland. We have a website at: www.brimvolt.com where you can get acquainted with our activities.
We require a double-sided flyer in A4 format to be handed out in conferences, trade shows etc. The flyer is basically a summarized overview of our range of services.

The deliverable should incorporate some visual elements that are relevant to our line of business such as:
• computers
• cybersecurity
• networks
Also, it would be nice to have visuals relating to Icelandic geography, to further emphasize our local roots. Some suggested keywords:
• volcano
• aurora borealis
• waterfall
• glacier

NB: the flyer will be printed out, therefore image resolution needs to be high enough to render nicely on paper.
The primary colors would be red, black and white – in line with our logo. But there is freedom to diverge and go for a different color scheme.

The logo should be present on the top front of the flyer. The URL www.brimvolt.com needs to be mentioned prominently, for example at the bottom of the page.

Examples of design we like:
• https://www.pixelbazaar.net/design/24252027
• https://www.pixelbazaar.net/design/24291120

Attached:
• the text for the brochure in PDF format
• our logo in vector format

IT, software, cybersecurity

EB3D1F
EC4F4E
F09395
F8D3D4
FCEDEE

• existing logo, and visuals related to computer, networks etc
• Icelandic geography/landscapes

```html
<!DOCTYPE html>
<html lang="en">
<head>
<meta charset="utf-8">
<title>Brimvolt flyer – front and back</title>
<link rel="stylesheet" href="https://fonts.googleapis.com/css2?family=Montserrat:wght@400;500;600;700;800&display=swap">
<style>
:root{
  --stage:#6e6e6e;
  --paper:#ffffff;
  --red:#a30d0d;
  --red-deep:#7a0505;
  --red-bright:#c4161c;
  --ink:#1a1a1a;
  --black:#070707;
  --text-light:#f3f3f3;
}
*{box-sizing:border-box;margin:0;padding:0}
html,body{width:1200px;height:1200px;overflow:hidden}
body{background:var(--stage);font-family:"Montserrat",sans-serif;color:var(--ink);position:relative}
.page{position:absolute;left:407px;width:386px;height:543px;background:var(--paper);overflow:hidden}
.page--front{top:31px}
.page--back{top:615px;height:542px}
.brand{position:absolute;left:233px;top:11px;height:28px;display:flex;align-items:center;gap:5px}
.brand__dot{width:26px;height:26px;border-radius:50%;background:var(--red-bright)}
.brand__name{font-weight:800;font-size:15px;letter-spacing:.5px;color:var(--ink)}
.hero-panel{position:absolute;left:0;top:26px;width:205px;height:162px;border-radius:0 7px 7px 0;
  background:radial-gradient(circle at 85% 20%,#b3141a 0,var(--red-deep) 55%,#5e0303 100%);color:#fff}
.hero-photo{position:absolute;left:208px;top:47px;width:178px;height:141px;border-radius:8px 0 0 0}
.hero-photo--ops{background:linear-gradient(135deg,#0b1a33,#1d4a86 45%,#0a1426)}
.hero-photo--team{background:linear-gradient(135deg,#6c7a8a,#cfd4d8 50%,#8d7f70)}
.hero-title{position:absolute;left:22px;top:27px;font-size:16.5px;line-height:17.5px;font-weight:400;letter-spacing:-.2px}
.hero-title b{font-weight:800}
.hero-title .big{font-size:21px;font-weight:800;line-height:22px;display:block;margin-top:1px}
.hero-lead{position:absolute;left:22px;top:113px;width:170px;font-size:6.8px;line-height:8.8px}
.cols{position:absolute;left:0;width:386px;display:flex}
.cols--light{top:199px;height:146px}
.cols--dark{top:347px;height:162px;background:linear-gradient(120deg,#1a0606,#3d0808 40%,#0d0d0d 70%,#2a0707);color:var(--text-light)}
.col{position:relative;width:193px;padding-left:39px;padding-right:12px}
.col + .col{padding-left:12px;padding-right:28px}
.col + .col::before{content:"";position:absolute;left:0;top:0;bottom:8px;width:1px;background:var(--red-bright)}
.icon{display:block;width:38px;height:38px;margin:0 0 0 24px}
.col + .col .icon{margin-left:45px}
.svc-title{font-size:10.5px;line-height:11px;font-weight:700;color:var(--red);margin-top:8px}
.cols--dark .svc-title{color:#fff}
.svc-body{font-size:5.3px;line-height:7px;margin-top:5px}
.cols--light .col + .col .svc-body{font-size:5.6px;line-height:7.6px}
.svc-tag{font-size:5.6px;font-weight:700;color:var(--red);margin-top:7px}
.cols--dark .svc-tag{color:#fff}
.cols--dark .svc-body{font-size:5.6px;line-height:7.6px}
.footer{position:absolute;left:0;bottom:0;width:386px;height:37px;border-top:3px solid var(--red-bright);display:flex}
.footer__phone{width:193px;background:var(--red);color:#fff;display:flex;align-items:center;justify-content:center;gap:9px;font-weight:800;font-size:17.5px}
.footer__web{flex:1;background:var(--black);color:#fff;display:flex;flex-direction:column;align-items:flex-end;justify-content:center;padding-right:35px}
.footer__url{font-size:9px;font-weight:700;display:flex;align-items:center;gap:4px}
.footer__mail{font-size:7.5px;display:flex;align-items:center;gap:4px}
.auto-title{position:absolute;left:22px;top:36px;font-size:17.5px;font-weight:800}
.auto-body{position:absolute;left:21px;top:61px;width:173px;font-size:5.9px;line-height:7.6px;text-align:justify}
.auto-tag{position:absolute;left:21px;top:125px;font-size:5.8px;font-weight:700}
.feature{position:absolute;left:20px;width:350px;display:flex;gap:13px}
.feature--assess{top:209px}
.feature--security{top:288px}
.feature .icon{margin:0;flex:none}
.feature__title{font-size:14px;font-weight:700;color:var(--red);line-height:15px}
.feature__body{font-size:5.8px;line-height:7.6px;margin-top:4px;text-align:justify}
.feature__body + .feature__body{margin-top:7px}
.feature__tag{font-size:5.8px;font-weight:600;color:var(--red);margin-top:7px}
.office-photo{position:absolute;left:0;top:329px;width:386px;height:176px;
  background:linear-gradient(180deg,rgba(255,255,255,1) 0,rgba(220,228,236,.9) 30%,#8b97a5 75%,#5c6673 100%)}
.office-text{position:absolute;left:0;width:386px;top:474px;text-align:center;color:#fff;font-size:10.8px;line-height:12.5px;font-weight:500;letter-spacing:.4px}
.feature-content{padding-top:4px}
</style>
</head>
<body>

<svg width="0" height="0" style="position:absolute">
  <defs>
    <symbol id="ring" viewBox="0 0 38 38">
      <circle cx="19" cy="19" r="17.5" fill="#fff" stroke="#111" stroke-width="2"/>
      <path d="M3.5 23 A16 16 0 0 0 34.5 23" fill="none" stroke="#b3141a" stroke-width="2.6"/>
    </symbol>
  </defs>
</svg>

<!-- Front -->
<section class="page page--front">
  <div class="brand"><span class="brand__dot"></span><span class="brand__name">BRIMVOLT</span></div>
  <div class="hero-panel">
    <h1 class="hero-title">Your <b>Icelandic</b><br><b>Partner</b> in<br><b>Cybersecurity</b> and<span class="big">IT Consultancy</span></h1>
    <p class="hero-lead">We transform operational challenges into bespoke IT solutions. Ready to experience the power of innovative approaches?</p>
  </div>
  <div class="hero-photo hero-photo--ops" role="img" aria-label="Two analysts watching a large blue cybersecurity dashboard in a dark control room"></div>

  <div class="cols cols--light">
    <div class="col">
      <svg class="icon" viewBox="0 0 38 38"><use href="#ring"/><circle cx="19" cy="18" r="5" fill="none" stroke="#111" stroke-width="2"/><circle cx="19" cy="18" r="1.6" fill="#111"/><circle cx="12" cy="12" r="1.6" fill="#111"/><circle cx="26" cy="12" r="1.6" fill="#111"/><circle cx="12" cy="24" r="1.6" fill="#111"/><circle cx="26" cy="24" r="1.6" fill="#111"/></svg>
      <h2 class="svc-title">Brimvolt ehf –<br>Your Icelandic IT partner</h2>
      <p class="svc-body">Step into a world of comprehensive IT solutions tailored to your unique needs. Our services, available on a contract or as-needed basis, are designed to empower your business and equip you with the tools you need to succeed. More than just a list of offerings, they're a commitment to quality, a dedication to innovation, and a promise of reliability.</p>
    </div>
    <div class="col">
      <svg class="icon" viewBox="0 0 38 38"><use href="#ring"/><rect x="10" y="11" width="18" height="12" rx="1" fill="none" stroke="#111" stroke-width="1.8"/><path d="M16 15l-2 2 2 2M22 15l2 2-2 2M19.8 14.5l-1.6 5" fill="none" stroke="#111" stroke-width="1.2"/><path d="M15 27h8M19 23v4" stroke="#111" stroke-width="1.8"/></svg>
      <h2 class="svc-title">Software Development and Integration Services</h2>
      <p class="svc-body">We specialize in custom software development across different platforms (server, desktop, embedded systems). We are open source software advocates, and leverage decades of experience to deliver innovative and cost-effective solutions tailored to your needs.</p>
      <p class="svc-tag">Let's build the perfect software solution for you.</p>
    </div>
  </div>

  <div class="cols cols--dark" role="img" aria-label="Dark red-toned server room background">
    <div class="col">
      <svg class="icon" viewBox="0 0 38 38" style="margin-top:9px"><use href="#ring"/><circle cx="17" cy="12" r="3.5" fill="#111"/><rect x="11" y="17" width="13" height="10" rx="1" fill="#111"/><circle cx="17.5" cy="22" r="1.5" fill="#fff"/><circle cx="26" cy="11" r="2.4" fill="none" stroke="#111" stroke-width="1.6"/></svg>
      <h2 class="svc-title">Systems Administration</h2>
      <p class="svc-body">Are you having trouble with your IT infrastructure and in need of qualified personnel to take care of them? Or do you simply need a watchful and expert eye to ensure your systems keep running smoothly? We provide on-site and remote sysadmin services to manage your systems and bring you peace of mind.</p>
      <p class="svc-tag">Take back control.</p>
    </div>
    <div class="col">
      <svg class="icon" viewBox="0 0 38 38" style="margin-top:9px"><use href="#ring"/><rect x="10" y="10" width="18" height="13" rx="1" fill="none" stroke="#111" stroke-width="1.8"/><circle cx="16" cy="16" r="2.6" fill="none" stroke="#111" stroke-width="1.3"/><path d="M14 18l-2 2M21 19v-4M23 19v-6M25 19v-3" stroke="#111" stroke-width="1.2"/><path d="M15 27h8M19 23v4" stroke="#111" stroke-width="1.8"/></svg>
      <h2 class="svc-title">Infrastructure Monitoring Services</h2>
      <p class="svc-body">Do you know what is really going on inside your systems? We leverage leading open source monitoring solutions to bring visibility to your infrastructure. Monitor your systems proactively to ensure that they remain healthy at all times. Collect logs in real time and be notified when problems occur or warnings are raised.</p>
      <p class="svc-tag">Fix issues before they become problems.<br>Take back control.</p>
    </div>
  </div>

  <footer class="footer">
    <div class="footer__phone">
      <svg width="12" height="20" viewBox="0 0 12 20"><rect x="1" y="1" width="10" height="18" rx="2" fill="none" stroke="#fff" stroke-width="1.6"/><path d="M4 16h4" stroke="#fff" stroke-width="1.4"/></svg>
      +354 5550147
    </div>
    <div class="footer__web">
      <span class="footer__url"><svg width="8" height="8" viewBox="0 0 10 10"><circle cx="5" cy="5" r="4.2" fill="none" stroke="#c4161c" stroke-width="1.2"/><path d="M1 5h8M5 1v8" stroke="#c4161c" stroke-width=".9"/></svg>www.brimvolt.com</span>
      <span class="footer__mail"><svg width="8" height="6" viewBox="0 0 10 7"><rect x=".5" y=".5" width="9" height="6" fill="none" stroke="#c4161c"/><path d="M.5 .5l4.5 3.5 4.5-3.5" fill="none" stroke="#c4161c"/></svg>info@brimvolt.com</span>
    </div>
  </footer>
</section>

<!-- Back -->
<section class="page page--back">
  <div class="brand"><span class="brand__dot"></span><span class="brand__name">BRIMVOLT</span></div>
  <div class="hero-panel">
    <h2 class="auto-title">Automation</h2>
    <p class="auto-body">Because you need effective tools to grow and prosper, it is essential that your IT systems align with your operational needs. We offer a comprehensive review of your business and IT environment so as to optimize the means already at your disposal. We streamline your workflow and develop new tools as needed, to make your IT systems work harder for you.</p>
    <p class="auto-tag">Let us automate the boring stuff for you.</p>
  </div>
  <div class="hero-photo hero-photo--team" role="img" aria-label="Team of colleagues in a bright office with a laptop showing analytics charts"></div>

  <div class="feature feature--assess">
    <svg class="icon" viewBox="0 0 38 38"><use href="#ring"/><circle cx="17" cy="19" r="6" fill="none" stroke="#111" stroke-width="2.4" stroke-dasharray="3 2"/><path d="M23 15h5M23 19h6M23 23h5" stroke="#111" stroke-width="1.4"/><circle cx="29" cy="15" r="1.3" fill="#111"/><circle cx="30" cy="23" r="1.3" fill="#111"/></svg>
    <div class="feature-content">
      <h2 class="feature__title">Technology Assessment Services</h2>
      <p class="feature__body">Unsure about which tools are right for you or what IT strategy to pursue to help your business grow? We conduct market research and perform technical evaluations of software and hardware products to determine the best solutions for your company.</p>
      <p class="feature__tag">Let's empower your business with leading-edge solutions.</p>
    </div>
  </div>

  <div class="office-photo" role="img" aria-label="Bright modern office with two colleagues working together at a computer"></div>

  <div class="feature feature--security">
    <svg class="icon" viewBox="0 0 38 38"><use href="#ring"/><path d="M19 10l7 3v5c0 5-3 8-7 10-4-2-7-5-7-10v-5z" fill="#111"/><path d="M19 12v14c3-1.6 5-4 5-8v-3.6z" fill="#fff"/></svg>
    <div class="feature-content">
      <h2 class="feature__title">Security Services</h2>
      <p class="feature__body">We understand the importance of security in today's digital landscape. That's why we offer comprehensive security services, including network audits to find and remedy flaws before they can be exploited to your disadvantage.</p>
      <p class="feature__body">We perform a thorough review of your IT environment to identify and remediate the weak spots, in order to keep your business secure, protect your assets and your reputation. Let's raise your security posture to the highest standards, so that you don't become the next victim - or headline.</p>
      <p class="feature__tag">Bring the good guys in to keep the bad guys out.</p>
    </div>
  </div>

  <p class="office-text">Get in touch with us today to<br>discuss your IT needs in strict confidence.</p>

  <footer class="footer">
    <div class="footer__phone">
      <svg width="12" height="20" viewBox="0 0 12 20"><rect x="1" y="1" width="10" height="18" rx="2" fill="none" stroke="#fff" stroke-width="1.6"/><path d="M4 16h4" stroke="#fff" stroke-width="1.4"/></svg>
      +354 5550147
    </div>
    <div class="footer__web" style="padding-right:27px">
      <span class="footer__url"><svg width="8" height="8" viewBox="0 0 10 10"><circle cx="5" cy="5" r="4.2" fill="none" stroke="#c4161c" stroke-width="1.2"/><path d="M1 5h8M5 1v8" stroke="#c4161c" stroke-width=".9"/></svg>www.brimvolt.com</span>
      <span class="footer__mail"><svg width="8" height="6" viewBox="0 0 10 7"><rect x=".5" y=".5" width="9" height="6" fill="none" stroke="#c4161c"/><path d="M.5 .5l4.5 3.5 4.5-3.5" fill="none" stroke="#c4161c"/></svg>info@brimvolt.com</span>
    </div>
  </footer>
</section>

</body>
</html>
```